KPV Rock Bucket advertisement/ interactive flyer

We are looking for a promotional flyer in PDF form. Target audience would be BRANDOWICKE, Morevane, PWL Etc. emphasis to be on British design & build. Company logo attached. Possibility of full product catalog to be designed

Target Market(s)

Sales teams at BRANDOWICKE, morevane, PWL etc..

Industry/Entity Type

Heavy plant, excavation, construction, demolition, quarry

Requirements
Must have
• Must have reference to TLKE VANTREL steels. Vantrel 450 & Vantrel 500 . Must also ensure people know this bucket is British.
Nice to have
• Tagged components that can link back to TLKE web pages.

```html
<!DOCTYPE html>
<html lang="en">
<head>
<meta charset="utf-8">
<title>Brenmoor Engineering – Rock Bucket Flyer</title>
<link href="https://fonts.googleapis.com/css2?family=Montserrat:wght@600;700;800&family=Poppins:wght@400;500;600;700&display=swap" rel="stylesheet">
<style>
  :root {
    --brand-yellow: #f7b80f;
    --brand-charcoal: #3a3a3a;
    --footer-charcoal: #3b3b3b;
    --ink: #333333;
    --paper: #ffffff;
    --backdrop: #b3b1b3;
    --photo-dark: #2c2c2c;
    --photo-light: #d8d8d8;
    --steel-blue: #56606e;
    --steel-sky: #a9b4c2;
  }
  * { box-sizing: border-box; margin: 0; padding: 0; }
  html, body { width: 857px; height: 1200px; overflow: hidden; background: var(--backdrop); }
  body { font-family: "Poppins", sans-serif; color: var(--ink); }

  .stage { position: relative; width: 857px; height: 1200px; background: var(--backdrop); overflow: hidden; }

  .page {
    position: absolute; top: 318px; width: 857px; height: 1200px;
    background: var(--paper); overflow: hidden;
    transform: scale(0.47); transform-origin: 0 0;
    box-shadow: 0 20px 40px rgba(0,0,0,0.35);
  }
  .page--company { left: 17px; }
  .page--product { left: 437px; }

  /* ---------- shared ---------- */
  .section-tag { position: absolute; left: 0; height: 30px; padding: 0 24px 0 36px; background: var(--brand-yellow); border-radius: 0 15px 15px 0; color: var(--paper); font-family: "Montserrat", sans-serif; font-weight: 700; font-size: 17px; line-height: 30px; white-space: nowrap; }

  .body-copy { position: absolute; left: 36px; width: 460px; font-size: 12.2px; line-height: 1.5; }
  .body-copy--strong { font-weight: 600; font-size: 13.2px; line-height: 1.45; color: #222; }

  .product-shot { position: absolute; left: 527px; width: 292px; height: 157px; }
  .product-shot--a { top: 604px; }
  .product-shot--b { top: 778px; }
  .product-shot--c { top: 953px; }
  .tone-grey { background: linear-gradient(160deg, var(--steel-sky) 0%, var(--steel-blue) 45%, #7d6f5a 100%); }
  .tone-grey-back { background: linear-gradient(170deg, var(--steel-sky) 0%, #4f5968 50%, #8a7c63 100%); }
  .tone-worn { background: linear-gradient(160deg, #b3bcc8 0%, #5a3a2e 45%, #c79a4a 100%); }

  .contact-bar { position: absolute; left: 0; top: 1152px; width: 857px; height: 48px; background: var(--footer-charcoal); border-top: 5px solid var(--brand-yellow); display: flex; align-items: center; justify-content: space-between; padding: 0 36px; color: var(--paper); font-size: 12.5px; }
  .contact-bar__item { display: flex; align-items: center; gap: 8px; }
  .contact-bar__icon { width: 13px; height: 13px; }

  /* ---------- company page ---------- */
  .hero { position: absolute; left: 0; top: 0; width: 857px; height: 560px; }
  .brand-mark { position: absolute; left: 36px; top: 58px; display: flex; align-items: center; gap: 12px; }
  .brand-mark__square { width: 34px; height: 34px; background: var(--brand-yellow); flex: none; }
  .brand-mark__name { font-family: "Montserrat", sans-serif; font-weight: 700; font-size: 24px; line-height: 1.05; letter-spacing: 0.5px; color: var(--brand-charcoal); }

  .hero__intro { position: absolute; left: 35px; top: 218px; width: 400px; color: var(--paper); }
  .hero__title { font-family: "Montserrat", sans-serif; font-weight: 700; font-size: 40px; line-height: 1.08; color: var(--brand-yellow); margin-bottom: 16px; }
  .hero__text { font-size: 12.2px; line-height: 1.38; margin-bottom: 14px; }

  .feature-list { position: absolute; left: 36px; top: 778px; list-style: none; }
  .feature-list li { position: relative; padding-left: 18px; font-size: 13.4px; height: 30px; line-height: 30px; }
  .feature-list li::before { content: ""; position: absolute; left: 0; top: 10px; width: 10px; height: 10px; border-radius: 50%; background: var(--brand-yellow); }

  /* ---------- product page ---------- */
  .product-hero { position: absolute; left: 0; top: 0; width: 857px; height: 544px; background: linear-gradient(180deg, #b9c3cf 0%, #a4afbd 35%, #5e4638 62%, #8a7a66 80%, #a89a86 100%); }
  .product-rule { position: absolute; left: 0; top: 550px; width: 857px; height: 5px; background: var(--brand-yellow); }
  .logo-box { position: absolute; left: 44px; top: 0; width: 203px; height: 200px; background: var(--brand-charcoal); display: flex; flex-direction: column; align-items: center; justify-content: center; gap: 14px; }
  .logo-box__square { width: 40px; height: 40px; background: var(--brand-yellow); }
  .logo-box__name { font-family: "Montserrat", sans-serif; font-weight: 700; font-size: 21px; line-height: 1.1; color: var(--paper); text-align: center; letter-spacing: 0.5px; }

  .lead-title { position: absolute; left: 36px; top: 598px; width: 400px; font-family: "Poppins", sans-serif; font-weight: 700; font-size: 13px; line-height: 1.4; text-transform: uppercase; color: #2a2a2a; }
  .lead-title::after { content: ""; display: block; width: 62px; height: 3px; margin-top: 3px; background: var(--brand-yellow); }
  .lead-copy { position: absolute; left: 36px; top: 650px; width: 395px; font-size: 12px; line-height: 1.4; }

  .section-tag--features { top: 766px; }
  .spec-list { position: absolute; left: 36px; top: 801px; list-style: none; }
  .spec-list li { position: relative; padding-left: 18px; font-size: 12.4px; font-weight: 500; text-transform: uppercase; height: 30.4px; line-height: 30.4px; }
  .spec-list li::before { content: ""; position: absolute; left: 0; top: 10px; width: 10px; height: 10px; border-radius: 50%; background: var(--brand-yellow); }

  .sub-title { position: absolute; left: 36px; top: 1064px; font-family: "Poppins", sans-serif; font-weight: 600; font-size: 17px; line-height: 1.2; color: #2a2a2a; }
  .sub-title::after { content: ""; display: block; width: 100%; height: 2px; margin-top: 1px; background: var(--brand-yellow); }
  .grade-grid { position: absolute; left: 36px; top: 1097px; display: grid; grid-template-columns: 120px 90px 110px; row-gap: 4px; list-style: none; }
  .grade-grid li { position: relative; padding-left: 12px; font-size: 9.6px; line-height: 13px; }
  .grade-grid li::before { content: ""; position: absolute; left: 0; top: 3.5px; width: 6px; height: 6px; border-radius: 50%; background: var(--brand-yellow); }
</style>
</head>
<body>
<main class="stage">

  <!-- Company page -->
  <article class="page page--company">
    <svg class="hero" width="857" height="560" viewBox="0 0 857 560">
      <defs>
        <linearGradient id="workshopTone" x1="0" y1="0" x2="1" y2="1">
          <stop offset="0" stop-color="#2c2c2c"/>
          <stop offset="0.45" stop-color="#d8d8d8"/>
          <stop offset="1" stop-color="#2c2c2c"/>
        </linearGradient>
      </defs>
      <polygon role="img" aria-label="Black and white photo of a welder working inside a large excavator bucket"
               points="334,0 857,0 857,322 612,538 603,538" fill="url(#workshopTone)"/>
      <polygon points="0,150 392,150 598,544 0,544" fill="#3a3a3a"/>
      <polyline points="0,553 619,553 857,340" fill="none" stroke="#f7b80f" stroke-width="4"/>
    </svg>

    <div class="brand-mark">
      <span class="brand-mark__square"></span>
      <span class="brand-mark__name">BRENMOOR<br>ENGINEERING</span>
    </div>

    <section class="hero__intro">
      <h1 class="hero__title">BRENMOOR<br>ENGINEERING</h1>
      <p class="hero__text">Rock buckets designed and built in Britain for heavy plant, excavation, construction, demolition and quarry work.</p>
      <p class="hero__text">Every bucket is cut, welded and finished in our own British workshop from TLKE Vantrel 450 and Vantrel 500 wear-resistant steels, giving a longer working life in the hardest ground and less time off the machine.</p>
    </section>

    <h2 class="section-tag" style="top:604px;">ABOUT US :</h2>
    <p class="body-copy" style="top:642px;">A British engineering business building heavy-duty rock buckets for dealers, hire fleets and contractors across the UK.</p>
    <p class="body-copy body-copy--strong" style="top:696px;">Designed and built in Britain from TLKE Vantrel 450 and Vantrel 500 wear-resistant steels for quarry, demolition and heavy excavation.</p>

    <ul class="feature-list">
      <li>Vantrel 450 body and wrapper plates.</li>
      <li>Vantrel 500 cutting edges</li>
      <li>Bolt-on wear buttons and heel</li>
      <li>Heavy duty side cutters.</li>
      <li>Made to order in Britain.</li>
    </ul>

    <h2 class="section-tag" style="top:942px;">OUR MISSION :</h2>
    <p class="body-copy" style="top:980px;">To build the toughest rock buckets on the market here in Britain, using proven TLKE Vantrel steels and skilled British fabricators, so that every bucket we supply works harder and lasts longer on site.</p>
    <p class="body-copy" style="top:1068px;">We work with sales teams and plant owners to match each bucket to the machine, the ground and the job, backed by honest advice and fast support.</p>

    <div class="product-shot product-shot--a tone-grey" role="img" aria-label="Photo of a painted grey rock bucket standing on a gravel yard"></div>
    <div class="product-shot product-shot--b tone-grey-back" role="img" aria-label="Photo of the back of a grey rock bucket on a site"></div>
    <div class="product-shot product-shot--c tone-worn" role="img" aria-label="Photo of a worn rock bucket with yellow teeth on open ground"></div>

    <footer class="contact-bar">
      <span class="contact-bar__item"><svg class="contact-bar__icon" viewBox="0 0 14 14"><circle cx="7" cy="7" r="7" fill="#f7b80f"/><path d="M4.5 4 l1.5 0 l.6 1.8 l-.9 .7 a4.5 4.5 0 0 0 1.8 1.8 l.7 -.9 l1.8 .6 l0 1.5 a5.5 5.5 0 0 1 -5.5 -5.5z" fill="#3b3b3b"/></svg>+000 0000 0000</span>
      <span class="contact-bar__item"><svg class="contact-bar__icon" viewBox="0 0 14 14"><circle cx="7" cy="7" r="7" fill="#f7b80f"/><rect x="3.5" y="4.5" width="7" height="5" fill="none" stroke="#3b3b3b" stroke-width="1"/><path d="M3.5 4.5 L7 7.3 L10.5 4.5" fill="none" stroke="#3b3b3b" stroke-width="1"/></svg>youremail@mailbox.com</span>
      <span class="contact-bar__item"><svg class="contact-bar__icon" viewBox="0 0 14 14"><circle cx="7" cy="7" r="7" fill="#f7b80f"/><path d="M7 3 a2.6 2.6 0 0 1 2.6 2.6 c0 1.8 -2.6 4.6 -2.6 4.6 s-2.6 -2.8 -2.6 -4.6 A2.6 2.6 0 0 1 7 3z" fill="#3b3b3b"/></svg>yourcompany address</span>
      <span class="contact-bar__item"><svg class="contact-bar__icon" viewBox="0 0 14 14"><circle cx="7" cy="7" r="7" fill="#f7b80f"/><circle cx="7" cy="7" r="3.6" fill="none" stroke="#3b3b3b" stroke-width="1"/><path d="M3.4 7 H10.6 M7 3.4 V10.6" stroke="#3b3b3b" stroke-width="0.8"/></svg>www.yourwebsite.com</span>
    </footer>
  </article>

  <!-- Product page -->
  <article class="page page--product">
    <div class="product-hero" role="img" aria-label="Low angle photo of a large worn rock bucket with wear buttons and yellow teeth under a cloudy sky"></div>
    <div class="product-rule"></div>

    <div class="logo-box">
      <span class="logo-box__square"></span>
      <span class="logo-box__name">BRENMOOR<br>ENGINEERING</span>
    </div>

    <h2 class="lead-title">British designed &amp; built rock buckets in TLKE Vantrel 450 &amp; 500 steel.</h2>
    <p class="lead-copy">Every bucket is designed and fabricated in Britain from TLKE Vantrel 450 and Vantrel 500 wear-resistant steels. The result is a stronger, lighter bucket that holds its shape in rock, keeps its edge for longer and spends more hours digging, with bolt-on wear parts that are quick to change on site.</p>

    <h2 class="section-tag section-tag--features">KEY FEATURES :</h2>
    <ul class="spec-list">
      <li>Vantrel 450 body and wrapper plates throughout.</li>
      <li>Vantrel 500 cutting edges</li>
      <li>British designed and built in</li>
      <li>Fully welded heavy duty side cutters.</li>
      <li>Bolt-on wear buttons.</li>
      <li>Replaceable teeth and a</li>
      <li>Reinforced heel and wear strips.</li>
      <li>Tailored to your machine and bucket linkage.</li>
    </ul>

    <h3 class="sub-title">STEEL GRADES :</h3>
    <ul class="grade-grid">
      <li>Vantrel 450</li><li>Vantrel 500</li><li>Made in UK</li>
      <li>Body plates</li><li>Edges</li><li>To order</li>
    </ul>

    <div class="product-shot product-shot--a tone-worn" role="img" aria-label="Photo of a worn rock bucket with wear buttons in a yard"></div>
    <div class="product-shot product-shot--b tone-grey" role="img" aria-label="Photo of a grey rock bucket with yellow teeth"></div>
    <div class="product-shot product-shot--c tone-grey-back" role="img" aria-label="Photo of a grey rock bucket resting on gravel"></div>

    <footer class="contact-bar">
      <span class="contact-bar__item"><svg class="contact-bar__icon" viewBox="0 0 14 14"><circle cx="7" cy="7" r="7" fill="#f7b80f"/><path d="M4.5 4 l1.5 0 l.6 1.8 l-.9 .7 a4.5 4.5 0 0 0 1.8 1.8 l.7 -.9 l1.8 .6 l0 1.5 a5.5 5.5 0 0 1 -5.5 -5.5z" fill="#3b3b3b"/></svg>+000 0000 0000</span>
      <span class="contact-bar__item"><svg class="contact-bar__icon" viewBox="0 0 14 14"><circle cx="7" cy="7" r="7" fill="#f7b80f"/><rect x="3.5" y="4.5" width="7" height="5" fill="none" stroke="#3b3b3b" stroke-width="1"/><path d="M3.5 4.5 L7 7.3 L10.5 4.5" fill="none" stroke="#3b3b3b" stroke-width="1"/></svg>youremail@mailbox.com</span>
      <span class="contact-bar__item"><svg class="contact-bar__icon" viewBox="0 0 14 14"><circle cx="7" cy="7" r="7" fill="#f7b80f"/><path d="M7 3 a2.6 2.6 0 0 1 2.6 2.6 c0 1.8 -2.6 4.6 -2.6 4.6 s-2.6 -2.8 -2.6 -4.6 A2.6 2.6 0 0 1 7 3z" fill="#3b3b3b"/></svg>yourcompany address</span>
      <span class="contact-bar__item"><svg class="contact-bar__icon" viewBox="0 0 14 14"><circle cx="7" cy="7" r="7" fill="#f7b80f"/><circle cx="7" cy="7" r="3.6" fill="none" stroke="#3b3b3b" stroke-width="1"/><path d="M3.4 7 H10.6 M7 3.4 V10.6" stroke="#3b3b3b" stroke-width="0.8"/></svg>www.yourwebsite.com</span>
    </footer>
  </article>

</main>
</body>
</html>
```